Summit Brightway Realty Group & Greenleaf Lending Services, Inc.
Present Our
Annual Holiday Celebration

for Agents, Originators, Clients & Friends
All are Welcome!!

Catered by Chef Ramo Ramo
w/ DJ and Full Dance Floor

** No Cover Charge
Saturday, January 22, 2022
7 pm - 11 pm

at Velvet Parlor
4871 Q Street NE Washington DC 20019

Call Marcus Pelletier at (240) 555-0184 with questions.

```html
<!DOCTYPE html>
<html lang="en">
<head>
<meta charset="utf-8">
<title>Annual Holiday Celebration</title>
<link href="https://fonts.googleapis.com/css2?family=Almendra:wght@400&family=Roboto:wght@400;700&family=Playfair+Display:ital,wght@1,900&family=Kalam:wght@400&display=swap" rel="stylesheet">
<style>
:root{
  --gold:#a99a2c;
  --black:#231f20;
  --teal:#0a8699;
  --white:#ffffff;
  --ink:#222222;
}
*{margin:0;padding:0;box-sizing:border-box}
html,body{width:1200px;height:1200px;overflow:hidden;background:var(--white)}
.flyer{position:absolute;left:0;top:0;width:1010px;height:1010px;transform:scale(1.18812);transform-origin:0 0;background:var(--white);font-family:'Roboto',sans-serif;color:var(--ink);overflow:hidden}
.deco{position:absolute;left:0;top:0}
.brand-row{position:absolute;top:40px;left:0;width:1010px;display:flex;justify-content:center;gap:50px;align-items:center}
.brand{font-family:'Roboto',sans-serif;font-weight:700;font-size:14px;color:var(--ink);display:flex;align-items:center;gap:8px;white-space:nowrap}
.brand .mark{width:14px;height:14px;background:var(--teal);flex:none}
.brand .mark.round{border-radius:50%;background:var(--gold)}
.presents{position:absolute;top:133px;width:1010px;text-align:center;font-size:30px;color:var(--ink)}
.title{position:absolute;top:185px;width:1010px;text-align:center;font-family:'Almendra',serif;font-weight:400;color:var(--gold);font-size:80px;line-height:100px;letter-spacing:1px}
.audience{position:absolute;top:409px;left:0;width:1010px;height:178px;background:var(--gold)}
.for-tag{position:absolute;left:470px;top:-12px;width:72px;height:40px;background:var(--white);border-radius:0 0 22px 22px;text-align:center;font-size:30px;line-height:36px;color:var(--ink)}
.group{position:absolute;top:40px;width:336px;text-align:center;color:var(--white);font-size:22px}
.group svg{display:block;margin:0 auto 22px}
.divider{position:absolute;top:44px;width:2px;height:130px;background:var(--white)}
.chef-photo{position:absolute;left:732px;top:604px;width:262px;height:406px;background:linear-gradient(180deg,#8c7b6a 0%,#cfc8bd 45%,#e6e2da 100%);border-radius:110px 110px 0 0;z-index:1}
.welcome{position:absolute;top:596px;left:0;width:1010px;text-align:center;font-family:'Playfair Display',serif;font-style:italic;font-weight:900;font-size:54px;color:var(--gold);padding-right:10px;z-index:2}
.welcome-rule{position:absolute;top:666px;left:0;width:1010px;height:5px;background:var(--gold)}
.contact{position:absolute;left:0;top:681px;width:504px;height:163px;background:var(--teal);color:var(--white);text-align:center}
.contact .lead{position:absolute;top:12px;width:100%;font-size:28px;padding-left:34px}
.contact .phone{position:absolute;top:46px;width:100%;font-size:54px;font-weight:700;padding-left:34px}
.contact .tail{position:absolute;top:115px;width:100%;font-size:28px;padding-left:34px}
.contact .cover{position:absolute;left:-38px;top:72px;transform:rotate(-90deg);font-size:15px;white-space:nowrap}
.catering{position:absolute;left:521px;top:690px;font-family:'Kalam',cursive;font-size:25px;line-height:30px;color:var(--ink);z-index:2}
.date-band{position:absolute;left:0;top:852px;width:1010px;height:95px}
.date-text{position:absolute;left:90px;top:858px;width:600px;text-align:center;color:var(--white);font-weight:700;font-size:29px;line-height:40px;z-index:2}
.venue{position:absolute;left:28px;top:962px;font-size:20px;color:var(--ink);z-index:2}
</style>
</head>
<body>
<main class="flyer">
  <svg class="deco" width="1010" height="1010" viewBox="0 0 1010 1010" aria-hidden="true">
    <polygon points="0,0 90,0 197,174 0,174" fill="var(--gold)"/>
    <polygon points="0,0 78,0 173,160 0,160" fill="var(--black)"/>
    <polygon points="1010,0 920,0 813,174 1010,174" fill="var(--gold)"/>
    <polygon points="1010,0 932,0 837,160 1010,160" fill="var(--black)"/>
    <polygon points="0,254 129,307 0,360" fill="var(--gold)"/>
    <polygon points="0,270 92,307 0,344" fill="var(--black)"/>
    <polygon points="1010,254 881,307 1010,360" fill="var(--gold)"/>
    <polygon points="1010,270 918,307 1010,344" fill="var(--black)"/>
    <polygon points="0,852 1010,852 1010,947 0,947 89,900" fill="var(--teal)"/>
  </svg>

  <div class="brand-row">
    <div class="brand"><span class="mark"></span>Summit Brightway Realty Group</div>
    <div class="brand"><span class="mark round"></span>Greenleaf Lending Services, Inc.</div>
  </div>

  <p class="presents">Present Our</p>
  <h1 class="title">ANNUAL HOLIDAY<br>CELEBRATION</h1>

  <section class="audience">
    <div class="for-tag">for</div>
    <div class="group" style="left:0">
      <svg width="80" height="90" viewBox="0 0 80 90" fill="none" stroke="#fff" stroke-width="3.5">
        <circle cx="40" cy="32" r="18"/><path d="M18 34v-6a22 22 0 0 1 44 0v6"/><rect x="14" y="28" width="7" height="14" rx="3"/><rect x="59" y="28" width="7" height="14" rx="3"/><path d="M62 42c0 8-8 12-16 12"/><path d="M8 86c0-16 12-26 32-26s32 10 32 26z"/><path d="M32 60l8 12 8-12"/>
      </svg>AGENTS</div>
    <div class="divider" style="left:336px"></div>
    <div class="group" style="left:337px">
      <svg width="100" height="90" viewBox="0 0 100 90" fill="none" stroke="#fff" stroke-width="3.5">
        <circle cx="36" cy="32" r="17"/><path d="M6 86c0-18 12-28 30-28s30 10 30 28z"/><circle cx="76" cy="36" r="12"/><path d="M70 50h12v8H70z"/><path d="M76 29v14M80 31h-6a3 3 0 0 0 0 5h4a3 3 0 0 1 0 5h-6"/><path d="M76 14v6M62 20l4 4M90 20l-4 4"/>
      </svg>ORIGINATORS</div>
    <div class="divider" style="left:673px"></div>
    <div class="group" style="left:674px">
      <svg width="100" height="90" viewBox="0 0 100 90" fill="none" stroke="#fff" stroke-width="4">
        <circle cx="40" cy="28" r="17"/><path d="M10 84c0-22 12-34 30-34s30 12 30 34z"/><circle cx="72" cy="42" r="12"/><path d="M70 60c12 0 20 8 20 24H72"/>
      </svg>CLIENTS &amp; FRIENDS</div>
  </section>

  <div class="chef-photo" role="img" aria-label="Photo of the caterer, a chef in a white chef's jacket smiling with hands clasped"></div>

  <p class="welcome">All are Welcome!!</p>
  <div class="welcome-rule"></div>

  <section class="contact">
    <span class="cover">** No Cover Charge</span>
    <p class="lead">Call Marcus Pelletier at</p>
    <p class="phone">(240) 555-0184</p>
    <p class="tail">with questions.</p>
  </section>

  <p class="catering">Catered by<br>Chef Ramo Ramo<br>w/DJ and Full<br>Dance Floor</p>

  <p class="date-text">Saturday, January 22, 2022<br>7 pm - 11 pm</p>
  <p class="venue">At Velvet Parlor 4871 Q Street NE Washington DC 20019</p>
</main>
</body>
</html>
```